Redesign current business card for food company

i would like to redesign my business card. our company is food company, our product range from chips, juices, milk and etc (mostly dried food stuff).
I want o keep same logo but , the rest is open to new design.
you can check at our website about our company www.torvikeats.com

Target Market(s)

most of food company

Industry/Entity Type

Business

Contact Information for Business Card

I want to keep more to blue color...

Colors
3176b5
abd036

Requirements
Must have
• our old logo
Nice to have
• we do not mind to have nice material on bus card in order to accomplish nice design. for example: using spot uv, embossed and etc.

```html
<!DOCTYPE html>
<html lang="en">
<head>
<meta charset="utf-8">
<title>Torvik Business Card</title>
<link rel="stylesheet" href="https://fonts.googleapis.com/css2?family=Montserrat:wght@400;500;700;800&display=swap">
<style>
  :root {
    --indigo: #35339b;
    --cyan: #1ea7c8;
    --white: #ffffff;
    --backdrop: #e4e5ea;
    --card-shadow: 0 14px 30px rgba(20, 20, 50, 0.22);
  }
  * { margin: 0; padding: 0; box-sizing: border-box; }
  html, body { width: 1200px; height: 900px; overflow: hidden; }
  body {
    background: var(--backdrop);
    font-family: "Montserrat", Arial, sans-serif;
    position: relative;
  }
  .card {
    position: absolute;
    width: 620px;
    height: 354px;
    border-radius: 22px;
    overflow: hidden;
    box-shadow: var(--card-shadow);
  }
  .card-bottom-band {
    position: absolute;
    left: 0; right: 0; bottom: 0;
    height: 12px;
    display: flex;
    align-items: flex-end;
  }

  /* Front */
  .card-front { left: 80px; top: 60px; background: var(--white); }
  .front-wordmark {
    position: absolute;
    left: 0; right: 0; top: 92px;
    text-align: center;
    font-weight: 800;
    font-size: 120px;
    letter-spacing: -3px;
    color: var(--indigo);
    line-height: 1;
  }
  .front-url {
    position: absolute;
    right: 230px; bottom: 26px;
    font-size: 17px;
    font-weight: 500;
    color: var(--indigo);
    letter-spacing: 0.3px;
  }
  .card-front .band-indigo { width: 62%; height: 12px; background: var(--indigo); }
  .card-front .band-cyan { flex: 1; height: 7px; background: var(--cyan); }

  /* Back */
  .card-back { left: 500px; top: 486px; background: var(--indigo); color: var(--white); }
  .back-wordmark {
    position: absolute;
    left: 42px; top: 70px;
    font-weight: 800;
    font-size: 84px;
    letter-spacing: -2px;
    line-height: 1;
    color: var(--white);
  }
  .holder {
    position: absolute;
    right: 40px; top: 46px;
    text-align: right;
  }
  .holder-name { font-weight: 700; font-size: 19px; letter-spacing: 0.4px; }
  .holder-title { font-size: 14px; color: var(--cyan); margin-top: 2px; }
  .divider-main {
    position: absolute;
    left: 350px; right: 38px; top: 104px;
    height: 1px; background: var(--white);
  }
  .contact-list {
    position: absolute;
    left: 42px; bottom: 36px;
    list-style: none;
    padding-top: 10px;
    border-top: 1px solid var(--white);
    width: 250px;
  }
  .contact-list li {
    display: flex; align-items: center; gap: 10px;
    font-size: 14px; line-height: 19px;
  }
  .contact-list svg { width: 11px; height: 11px; flex: none; }
  .contact-list .accent { color: var(--cyan); }
  .company-address {
    position: absolute;
    right: 40px; bottom: 42px;
    text-align: right;
    font-size: 14px; line-height: 19px;
  }
  .card-back .band-white { width: 45%; height: 12px; background: var(--white); }
  .card-back .band-cyan { flex: 1; height: 12px; background: var(--cyan); }
</style>
</head>
<body>

<section class="card card-front">
  <div class="front-wordmark">torvik</div>
  <div class="front-url">www.torvikeats.com</div>
  <div class="card-bottom-band">
    <span class="band-indigo"></span><span class="band-cyan"></span>
  </div>
</section>

<section class="card card-back">
  <div class="back-wordmark">torvik</div>
  <div class="holder">
    <div class="holder-name">Daniel Marsh</div>
    <div class="holder-title">President</div>
  </div>
  <div class="divider-main"></div>

  <ul class="contact-list">
    <li>
      <svg viewBox="0 0 12 12" fill="#fff"><path d="M2.5 1l2 2.2-1 1.3a7 7 0 0 0 4 4l1.3-1 2.2 2-1.2 1.5C5 10.5 1.5 7 1 2.2z"/></svg>
      555 014 2288
    </li>
    <li>
      <svg viewBox="0 0 12 12" fill="#fff"><rect x="2" y="1" width="8" height="4"/><rect x="0.5" y="5" width="11" height="6" rx="1"/></svg>
      555 014 2277
    </li>
    <li>
      <svg viewBox="0 0 12 12" fill="none" stroke="#fff" stroke-width="1.4"><rect x="3" y="0.8" width="6" height="10.4" rx="1"/></svg>
      555 017 4391
    </li>
    <li>
      <svg viewBox="0 0 12 12" fill="none" stroke="#fff" stroke-width="1.3"><rect x="0.7" y="2.2" width="10.6" height="7.6"/><path d="M0.7 2.2L6 6.8l5.3-4.6"/></svg>
      daniel@torvikeats.com
    </li>
    <li>
      <svg viewBox="0 0 12 12" fill="none" stroke="#fff" stroke-width="1.2"><circle cx="6" cy="6" r="5"/><ellipse cx="6" cy="6" rx="2.2" ry="5"/><path d="M1 6h10"/></svg>
      <span>www.<span class="accent">torvikeats</span>.com</span>
    </li>
  </ul>

  <div class="company-address">
    Torvik Enterprises Corp.<br>
    840 Elm Row Fairview CA 90412
  </div>

  <div class="card-bottom-band">
    <span class="band-white"></span><span class="band-cyan"></span>
  </div>
</section>

</body>
</html>
```